Sports Performance Lab needs a new website

We need an updated/new website for Kelvora Human Performance Lab. We recently moved from Florida to the Chicago area. We perform testing ranging from VO2 Max, Lactate Threshold, Resting Metabolic Rate, Body Composition Testing with the VEXA SHELL and Metabolic Efficiency Testing. We also have a mobile lab contained in a 24 foot trailer. We work with athletes, coaches, Fitness Gyms, Dura Stride Gyms to improve performance and also with people looking to manage or lose weight. Our current site is www.kelvoralab-example.com. Looking for an improved site, better grahics/photos but also blends into our current logo and graphics on Mobile Lab. Would like a calendar/ appointment page on website

Colors
ec1f27
000000
fbed22

Requirements
Must have
• ability to easily updatae
Nice to have
• appointment calendar

```html
<!DOCTYPE html>
<html lang="en">
<head>
<meta charset="utf-8">
<title>Kelvora Human Performance Lab</title>
<link rel="stylesheet" href="https://fonts.googleapis.com/css2?family=Roboto:ital,wght@0,400;0,500;0,700;0,900;1,900&display=swap">
<style>
:root{
  --red:#ec1f27;
  --yellow:#fbed22;
  --ink:#111;
  --dark:#23282c;
  --darker:#1b1f22;
  --panel:#3a3f43;
  --grey:#666;
  --line:#bbb;
  --white:#fff;
  --footer-text:#d6d6d6;
}
*{box-sizing:border-box;margin:0;padding:0}
html,body{width:1200px;height:2985px;overflow:hidden}
body{font-family:"Roboto",Arial,sans-serif;color:var(--ink);background:var(--white);position:relative}
.abs{position:absolute}

/* header */
.site-header{position:absolute;left:0;top:0;width:1200px;height:124px;background:linear-gradient(90deg,#2c3034,#43484c 50%,#2c3034)}
.brand{position:absolute;left:100px;top:34px;display:flex;align-items:center;gap:12px;color:var(--white);font-weight:700}
.brand-mark{width:16px;height:16px;background:var(--yellow)}
.brand-name{font-size:30px;line-height:30px;letter-spacing:1px}
.brand-sub{font-size:11px;letter-spacing:1.5px;margin-top:4px;white-space:nowrap}
.call{position:absolute;left:760px;top:44px;display:flex;gap:14px;color:var(--white)}
.call-icon{width:40px;height:40px;background:#e6c500;display:flex;align-items:center;justify-content:center}
.call small{font-size:13px;display:block}
.call strong{font-size:19px;font-weight:500}
.btn-appointment{position:absolute;left:956px;top:44px;width:150px;height:40px;background:var(--red);color:var(--white);font-size:14px;font-weight:500;display:flex;align-items:center;justify-content:center;gap:10px}

/* nav */
.main-nav{position:absolute;left:0;top:124px;width:1200px;height:52px;background:var(--yellow)}
.main-nav a{position:absolute;top:0;height:52px;line-height:52px;font-size:13px;font-weight:700;color:var(--ink);text-decoration:none;white-space:nowrap}
.main-nav a.active{background:var(--red);color:var(--white);width:100px;text-align:center}

/* hero */
.hero{position:absolute;left:0;top:176px;width:1200px;height:452px;background:linear-gradient(110deg,#b49a86 0%,#6e5f57 35%,#3b3f47 65%,#232833 100%)}
.hero-title{position:absolute;left:260px;top:380px;width:686px;height:62px;background:rgba(25,25,25,.8);color:var(--white);font-style:italic;font-weight:900;font-size:34px;letter-spacing:.5px;text-align:center;line-height:58px;border-bottom:4px solid var(--yellow)}
.dots{position:absolute;left:576px;top:586px;display:flex;gap:6px}
.dots span{width:12px;height:12px;background:#bbb}
.dots span.on{background:var(--red)}

/* about */
.about h2{position:absolute;left:100px;top:670px;font-size:27px;font-weight:400}
h2 b{font-weight:700}
.about-text{position:absolute;left:100px;top:726px;width:650px;font-size:13.5px;line-height:25px;color:#222}
.about-text p+p{margin-top:6px}
.about-photo{position:absolute;left:770px;top:650px;width:336px;height:316px;background:linear-gradient(180deg,#f4f4f4 0%,#d8b49a 45%,#8e8f9a 100%)}

/* services */
.services{position:absolute;left:0;top:966px;width:1200px;height:536px;background:linear-gradient(180deg,#2e3336,#454a4e 55%,#33383b)}
.section-title{position:absolute;left:0;width:1200px;text-align:center;font-size:28px;font-weight:400}
.service-card{position:absolute;top:1096px;width:230px;height:284px;background:#3f4548}
.service-card .photo{height:160px}
.service-card h3{color:var(--yellow);font-size:19px;font-weight:400;margin:14px 14px 4px}
.service-card p{color:#eee;font-size:12.5px;line-height:21px;margin:0 14px}
.btn-red{position:absolute;background:var(--red);color:var(--white);font-size:13.5px;font-weight:500;display:flex;align-items:center;justify-content:center}
.services-contact{position:absolute;left:274px;top:1432px;color:#eee;font-size:13.5px}

/* tests */
.tests{position:absolute;left:0;top:1502px;width:1200px;height:764px;background:linear-gradient(90deg,#fff 0%,#f4f4f4 40%,#e6e6e6 70%,#f6f6f6 100%)}
.tests-intro{position:absolute;left:340px;top:1590px;width:520px;text-align:center;font-size:13px;line-height:23px;color:#333}
.test-card{position:absolute;width:230px;height:240px;background:var(--panel)}
.test-card .photo{height:160px}
.test-card h3{font-size:18.5px;font-weight:400;color:var(--yellow);margin:14px 16px 0;line-height:25px}
.test-card.highlight{background:var(--yellow)}
.test-card.highlight h3{color:#333}

/* membership */
.membership-intro{position:absolute;left:230px;top:2356px;width:740px;text-align:center;font-size:13.5px;line-height:24px;color:#333}
.field{position:absolute;height:26px;border-bottom:1px solid var(--line);font-size:13px;color:var(--grey)}

/* footer */
.site-footer{position:absolute;left:0;top:2674px;width:1200px;height:276px;background:var(--dark)}
.footer-col{color:var(--footer-text)}
.footer-col h4{position:absolute;top:2718px;color:var(--yellow);font-size:16px;font-weight:500}
.divider{position:absolute;top:2712px;width:1px;height:190px;background:#3c4247}
.quick-links{position:absolute;left:100px;top:2760px;list-style:none;font-size:12.5px;line-height:22.5px;color:var(--footer-text)}
.quick-links li::before{content:"";display:inline-block;width:3px;height:3px;background:#aaa;margin-right:10px;vertical-align:middle}
.newsletter-text{position:absolute;left:360px;top:2758px;width:200px;font-size:12.5px;line-height:20px;color:var(--footer-text)}
.newsletter-input{position:absolute;left:360px;top:2814px;width:186px;height:28px;background:var(--white);color:#999;font-size:12px;padding:7px 8px}
.contact-row{position:absolute;left:654px;display:flex;gap:12px;font-size:12.5px;line-height:19px;color:var(--footer-text)}
.contact-row svg{flex:none;margin-top:3px}
.footer-brand{position:absolute;left:930px;top:2746px;color:var(--white);font-weight:700;text-align:center;width:186px}
.footer-brand .brand-name{font-size:28px}
.footer-brand .brand-sub{font-size:9.5px;letter-spacing:1.2px}
.social{position:absolute;top:2828px;width:22px;height:22px;background:#4a5055;border-radius:2px}
.copyright{position:absolute;left:0;top:2950px;width:1200px;height:35px;background:var(--darker);color:#bbb;font-size:12px;text-align:center;line-height:35px}
</style>
</head>
<body>

<header class="site-header">
  <div class="brand">
    <span class="brand-mark"></span>
    <div><div class="brand-name">KELVORA</div><div class="brand-sub">HUMAN PERFORMANCE LAB</div></div>
  </div>
  <div class="call">
    <div class="call-icon">
      <svg width="18" height="18" viewBox="0 0 24 24"><path d="M6.6 10.8a15 15 0 0 0 6.6 6.6l2.2-2.2c.3-.3.7-.4 1-.2 1.1.4 2.3.6 3.6.6.6 0 1 .4 1 1V20c0 .6-.4 1-1 1A17 17 0 0 1 3 4c0-.6.4-1 1-1h3.5c.6 0 1 .4 1 1 0 1.3.2 2.5.6 3.6.1.3 0 .7-.2 1z" fill="var(--red)"/></svg>
    </div>
    <div><small>Call Us Now!</small><strong>(123) 456 7890</strong></div>
  </div>
  <div class="btn-appointment">
    <svg width="14" height="14" viewBox="0 0 14 14"><rect x="1" y="2" width="12" height="11" fill="none" stroke="#fff" stroke-width="1.5"/><line x1="1" y1="5.5" x2="13" y2="5.5" stroke="#fff" stroke-width="1.5"/></svg>
    Appointment
  </div>
</header>

<nav class="main-nav">
  <a class="active" style="left:100px">Home</a>
  <a style="left:230px">About Us</a>
  <a style="left:348px">Fitness Tests Services</a>
  <a style="left:536px">Vexa Shell</a>
  <a style="left:658px">Coaches Corner</a>
  <a style="left:818px">Corporate Wellness</a>
  <a style="left:1004px">Contact Us</a>
</nav>

<section class="hero" role="img" aria-label="Photo of an athlete doing a bench press with a spotter in a gym"></section>
<h1 class="hero-title">WORKOUTS CUSTOM TAILORED TO YOU</h1>
<div class="dots"><span class="on"></span><span></span></div>

<section class="about">
  <h2>About <b>Kelvora</b></h2>
  <div class="about-text">
    <p>Welcome to KELVORA - your source for mobile human performance testing including V02Max, Lactic Threshold, Metabolic Rate, Metabolic Efficiency, and Body Composition.</p>
    <p>We use state of the art equipment by Norvane including the Gold Standard VEXA SHELL in our completely self-contained mobile unit. Kelvora conducts both running and cycling assessments to ensure sport specific measurements to help you reach your peak performance goals. We also conduct body composition testing important for Dura Stride athletes and those participating in fitness competition, as well as critical in weight management programs.</p>
  </div>
  <div class="about-photo" role="img" aria-label="Photo of a fit woman and man in athletic wear"></div>
</section>

<section class="services" role="img" aria-label="Dark gym interior background photo"></section>
<h2 class="section-title" style="top:1014px;color:var(--yellow)">We Provide <b>Services</b></h2>
<article class="service-card" style="left:100px"><div class="photo" role="img" aria-label="Photo of a coach spotting a dumbbell press" style="background:linear-gradient(135deg,#8a8f93,#c94a3f)"></div><h3>Coaches</h3><p>It is a long established fact that a reader will be distracted by the readable content...</p></article>
<article class="service-card" style="left:360px"><div class="photo" role="img" aria-label="Photo of a woman doing sit-ups in a gym" style="background:linear-gradient(135deg,#9fc2d8,#4f7da0)"></div><h3>Fitness Gyms</h3><p>It is a long established fact that a reader will be distracted by the readable content...</p></article>
<article class="service-card" style="left:618px"><div class="photo" role="img" aria-label="Photo of an athlete flipping a large tire" style="background:linear-gradient(135deg,#5a5d60,#2d3033)"></div><h3>Dura Stride Gyms</h3><p>It is a long established fact that a reader will be distracted by the readable content...</p></article>
<article class="service-card" style="left:876px"><div class="photo" role="img" aria-label="Photo of a trainer measuring a woman's waist" style="background:linear-gradient(135deg,#3a3a3a,#b78f7c)"></div><h3>Lose Weight</h3><p>It is a long established fact that a reader will be distracted by the readable content...</p></article>
<div class="btn-red" style="left:100px;top:1422px;width:150px;height:38px">View All Services</div>
<div class="services-contact">Call us Now:&nbsp; (123) 456 7890 &nbsp;&nbsp; | &nbsp;&nbsp; Email:&nbsp; info@kelvoralab-example.com</div>

<section class="tests" role="img" aria-label="Faded photo of a woman running on a treadmill"></section>
<h2 class="section-title" style="top:1538px">Sports &amp; <b>Fitness Tests</b></h2>
<p class="tests-intro">Kelvora mobile Sports and Human Performance Testing Center services are for all levels of athletes and sports from triathlon to Dura Stride.</p>
<article class="test-card" style="left:100px;top:1674px"><div class="photo" role="img" aria-label="Photo of a man seated in a body composition chamber" style="background:linear-gradient(135deg,#cfd3d6,#8a7d72)"></div><h3>Body Composition Analysis (VEXA SHELL)</h3></article>
<article class="test-card highlight" style="left:360px;top:1674px"><div class="photo" role="img" aria-label="Photo of a woman during a resting metabolic rate test" style="background:linear-gradient(135deg,#b9b9b9,#6f6f6f)"></div><h3>Resting Metabolic Rate (RMR)</h3></article>
<article class="test-card" style="left:618px;top:1674px"><div class="photo" role="img" aria-label="Photo of a cyclist during a VO2 max test" style="background:linear-gradient(135deg,#e4e4e4,#8b5b4a)"></div><h3>VO2 Max Test</h3></article>
<article class="test-card" style="left:876px;top:1674px"><div class="photo" role="img" aria-label="Photo of a finger blood sample for lactate testing" style="background:linear-gradient(135deg,#f0a060,#7d6fa8)"></div><h3>Lactate Threshold Test</h3></article>
<article class="test-card" style="left:360px;top:1942px"><div class="photo" role="img" aria-label="Photo of a runner's shoes on a treadmill" style="background:linear-gradient(135deg,#c6c6c6,#4f8f6a)"></div><h3>Calories per Hour Metabolic Efficiency</h3></article>
<article class="test-card" style="left:618px;top:1942px"><div class="photo" role="img" aria-label="Split video frames of a swimmer for stroke analysis" style="background:linear-gradient(135deg,#4fa3c8,#1a2d55)"></div><h3>Video Analysis with Stridecam</h3></article>

<section class="membership">
  <h2 class="section-title" style="top:2300px">Kelvora <b>Membership</b></h2>
  <p class="membership-intro">It is a long established fact that a reader will be distracted by the readable content of a page when looking at its layout simply dummy text of the printing and typesetting industry.</p>
  <div class="field" style="left:248px;top:2436px;width:224px">Fist Name</div>
  <div class="field" style="left:518px;top:2436px;width:224px">Last Name</div>
  <div class="field" style="left:790px;top:2436px;width:170px">Select Date
    <svg class="abs" style="right:2px;top:2px" width="13" height="13" viewBox="0 0 14 14"><rect x="1" y="2" width="12" height="11" fill="none" stroke="#999" stroke-width="1.3"/><line x1="1" y1="5.5" x2="13" y2="5.5" stroke="#999" stroke-width="1.3"/></svg>
  </div>
  <div class="field" style="left:248px;top:2482px;width:332px">Your Email</div>
  <div class="field" style="left:626px;top:2482px;width:334px">Your Phone</div>
  <div class="field" style="left:248px;top:2526px;width:712px">Enter Your Message</div>
  <div class="btn-red" style="left:512px;top:2582px;width:182px;height:38px">Submit Appointment</div>
</section>

<footer class="site-footer"></footer>
<div class="footer-col">
  <h4 style="left:100px">Quick Links</h4>
  <ul class="quick-links"><li>About Us</li><li>Fitness Tests Services</li><li>Vexa Shell</li><li>Coaches Corner</li><li>Corporate Wellness</li><li>Contact Us</li></ul>
</div>
<div class="divider" style="left:294px"></div>
<div class="footer-col">
  <h4 style="left:360px">Newsletter</h4>
  <p class="newsletter-text">Subscribe to our Newsletter to get latest scoop right to your inbox</p>
  <div class="newsletter-input">Email Address</div>
  <div class="btn-red" style="left:360px;top:2856px;width:86px;height:26px;font-size:12.5px">Submit</div>
</div>
<div class="divider" style="left:606px"></div>
<div class="footer-col">
  <h4 style="left:654px">Contact Us</h4>
  <div class="contact-row" style="top:2762px">
    <svg width="12" height="16" viewBox="0 0 12 16"><path d="M6 0a6 6 0 0 0-6 6c0 4.5 6 10 6 10s6-5.5 6-10a6 6 0 0 0-6-6zm0 8.5A2.5 2.5 0 1 1 6 3.5a2.5 2.5 0 0 1 0 5z" fill="var(--red)"/></svg>
    <div>Kelvora<br>P.O.Box Simply dummy<br>printing, ZN&nbsp; 4R2 9L8</div>
  </div>
  <div class="contact-row" style="top:2830px">
    <svg width="13" height="13" viewBox="0 0 24 24"><path d="M6.6 10.8a15 15 0 0 0 6.6 6.6l2.2-2.2c.3-.3.7-.4 1-.2 1.1.4 2.3.6 3.6.6.6 0 1 .4 1 1V20c0 .6-.4 1-1 1A17 17 0 0 1 3 4c0-.6.4-1 1-1h3.5c.6 0 1 .4 1 1 0 1.3.2 2.5.6 3.6.1.3 0 .7-.2 1z" fill="var(--red)"/></svg>
    <div>(123) 456 789</div>
  </div>
  <div class="contact-row" style="top:2860px">
    <svg width="13" height="11" viewBox="0 0 13 11"><rect width="13" height="11" fill="var(--red)"/><path d="M0 0l6.5 5.5L13 0" fill="none" stroke="#fff" stroke-width="1.2"/></svg>
    <div>Info@kelvoralab-example.com</div>
  </div>
</div>
<div class="divider" style="left:878px"></div>
<div class="footer-brand">
  <div class="brand-name">KELVORA</div>
  <div class="brand-sub">HUMAN PERFORMANCE LAB</div>
</div>
<span class="social" style="left:962px" aria-label="Social link"></span>
<span class="social" style="left:998px" aria-label="Social link"></span>
<span class="social" style="left:1034px" aria-label="Social link"></span>
<span class="social" style="left:1070px" aria-label="Social link"></span>

<div class="copyright">Copyright @ 2016 Kelvora Lab, All Rights Reserved</div>

</body>
</html>
```